Veltrisk inc. Aviation website

we are looking for a very modern and luxury web design, we are an aviation based company and specialize in aircraft exports and setup of air services world wide.
we want the website to be unique, creative, luxurious, professional, and to make an statement.
we have attached the logo.
our business cards theme is black background with gold stamping, if that is the rout you want to take.
**The format we are looking for is Wordpress.**
**the website is www.veltriskinc-example.com**
** 3 pages:
1. home page: -overview/about us
-industry leading
- worldwide presence
- aerial support
2. products and services: -business aircrafts
-commercial aircrafts
-amphibious aircrafts
-operation setup
-maintenance & crew training
3. contact us
**our location: Marlow Fenwick Harbour Airfield, Hangar 6**
we do appreciate suggestions
Thank you all.
Target Market(s)
Aviation professionals, Aircraft import/export, airlines, air taxi operations
Industry/Entity Type
It Company
Number of Pages Required
3 page
Requirements
Must have
- must have a very modern and luxurious design, and must be aviation oriented, and must have the logo, must be professional looking and be animated.
Nice to have
- black, gold, and burgandy colour
Should not have
- should not be playful and cartoony.

```html
<!DOCTYPE html>
<html lang="en">
<head>
<meta charset="utf-8">
<title>Veltrisk inc. — Aviation</title>
<link href="https://fonts.googleapis.com/css2?family=Open+Sans:wght@400;600;700&family=Oswald:wght@400;500&display=swap" rel="stylesheet">
<style>
:root{
  --ink:#121212;
  --panel:#1b1b1b;
  --gold:#f2b705;
  --gold-deep:#d99a00;
  --red:#b3121b;
  --burgundy:#7a0c12;
  --white:#ffffff;
  --muted:#9a9a9a;
  --sky-a:#1f3a52;
  --sky-b:#6d8aa3;
}
*{margin:0;padding:0;box-sizing:border-box}
html,body{width:1200px;height:2552px;overflow:hidden}
body{background:var(--ink);font-family:"Open Sans",Arial,sans-serif;color:var(--white);position:relative}
.site-header{position:absolute;top:0;left:0;width:1200px;height:64px;background:rgba(10,10,10,.78);z-index:5;display:flex;align-items:center;justify-content:space-between;padding:0 140px}
.brand{display:flex;align-items:center;gap:10px;font-weight:700;font-size:24px;color:var(--gold)}
.brand-dot{width:22px;height:22px;border-radius:50%;background:var(--red)}
.main-nav{display:flex;gap:4px}
.main-nav a{color:var(--white);text-decoration:none;font-size:14px;padding:22px 22px;font-weight:600}
.main-nav a.active{background:var(--red)}
.hero{position:absolute;top:0;left:0;width:1200px;height:616px;background:linear-gradient(180deg,var(--sky-a) 0%,var(--sky-b) 45%,#8d96a0 70%,#3a3f46 100%)}
.hero-title{position:absolute;left:0;top:510px;width:1200px;text-align:center;font-size:29px;font-weight:700;line-height:40px;text-shadow:0 2px 6px rgba(0,0,0,.7)}
.hero-strip{position:absolute;top:616px;left:0;width:1200px;height:256px;display:flex}
.hero-strip .shot-a{width:604px;background:linear-gradient(135deg,#5d6a76,#c9ccd0 60%,#7c858e)}
.hero-strip .shot-b{width:596px;background:linear-gradient(160deg,#0f2136,#22466b 60%,#0b1726)}
.intro{position:absolute;top:872px;left:0;width:1200px;height:118px;background:#141414;display:flex;gap:40px;padding:20px 160px 0}
.intro-col{flex:1}
.intro-col h3{font-size:15px;font-weight:700;text-transform:uppercase;margin-bottom:10px}
.intro-col p{font-size:11px;color:var(--muted);line-height:16px}
.services{position:absolute;top:990px;left:0;width:1200px;height:640px;background:radial-gradient(circle at 600px 410px,#3a3a3a 0,#222 260px,#111 560px)}
.section-title{position:absolute;left:0;width:1200px;text-align:center;font-family:"Oswald",Arial,sans-serif;font-size:26px;letter-spacing:1px;text-transform:uppercase}
.section-title .gold{color:var(--gold)}
.section-title .red{color:var(--red)}
.title-mark{position:absolute;left:588px;width:24px;height:18px}
.services svg{position:absolute;top:0;left:0}
.testimonials{position:absolute;top:1630px;left:0;width:1200px;height:550px;background:radial-gradient(ellipse at 600px 250px,#c5161f 0,var(--red) 40%,var(--burgundy) 100%)}
.quote{position:absolute;font-size:12px;line-height:18px;padding:22px 26px;border-radius:4px}
.quote-dark{left:230px;top:160px;width:330px;height:140px;background:#2a1616;color:#d8c8c8}
.quote-gold{left:640px;top:140px;width:360px;height:130px;background:var(--gold);color:#3a1a00}
.quote::after{content:"";position:absolute;bottom:-14px;left:60px;border:14px solid transparent;border-bottom:0;border-top-color:inherit}
.quote-dark::after{border-top-color:#2a1616}
.quote-gold::after{border-top-color:var(--gold)}
.client{position:absolute;display:flex;align-items:center;gap:14px}
.avatar{width:70px;height:70px;border-radius:50%;border:3px solid var(--white);background:linear-gradient(135deg,#b98a6a,#5a3d2c)}
.client-name{font-size:13px;font-weight:700}
.stars{color:var(--gold);font-size:12px;letter-spacing:2px}
.slide-arrow{position:absolute;top:225px;width:32px;height:32px;border-radius:50%;background:var(--white);color:var(--red);font-weight:700;text-align:center;line-height:31px;font-size:18px}
.site-footer{position:absolute;top:2180px;left:0;width:1200px;height:332px;background:#0c0c0c;padding:50px 130px 0}
.foot-col{position:absolute;top:50px}
.foot-col h4{font-size:13px;font-weight:700;text-transform:uppercase;color:var(--red);margin-bottom:16px}
.foot-col h4 span{color:var(--white)}
.foot-col li{list-style:none;font-size:12px;color:#cfcfcf;margin-bottom:10px;padding-left:14px;position:relative}
.foot-col li::before{content:"";position:absolute;left:0;top:6px;width:5px;height:5px;background:var(--red)}
.contact-line{font-size:12px;color:#cfcfcf;margin-bottom:10px;display:flex;gap:8px;align-items:center}
.contact-line i{width:8px;height:8px;background:var(--red);border-radius:50%;display:inline-block}
.social{display:flex;gap:8px;margin-top:40px}
.social span{width:24px;height:24px;border-radius:50%;background:#3a6fb3}
.inquiry{left:680px;width:400px;height:250px;background:linear-gradient(90deg,#1a1a1a,#262626);padding:18px 22px}
.field{background:var(--white);height:26px;margin-bottom:10px;font-size:11px;color:#777;padding:5px 10px;width:170px}
.field-row{display:flex;gap:10px}
.field.wide{width:170px;height:40px}
.submit{width:84px;height:28px;background:var(--red);color:var(--white);font-size:12px;font-weight:700;text-align:center;line-height:28px}
.copyright{position:absolute;top:2512px;left:0;width:1200px;height:40px;background:var(--gold);color:#2a1d00;font-size:11px;text-align:center;line-height:40px}
</style>
</head>
<body>

<header class="site-header">
  <div class="brand"><span class="brand-dot"></span>Veltrisk inc.</div>
  <nav class="main-nav">
    <a class="active" href="#">Home</a>
    <a href="#">About Us</a>
    <a href="#">Product And Services</a>
    <a href="#">Contact Us</a>
  </nav>
</header>

<section class="hero" role="img" aria-label="Photo of a passenger jet parked at an airport gate at dusk">
  <h1 class="hero-title">We Are An Aviation Based Company And Specialize In Aircraft Exports<br>And Setup Of Air Services Worldwide</h1>
</section>

<div class="hero-strip">
  <div class="shot-a" role="img" aria-label="Photo of aircraft in a maintenance hangar"></div>
  <div class="shot-b" role="img" aria-label="Photo of aircraft flying over a world map"></div>
</div>

<section class="intro">
  <div class="intro-col">
    <h3>Aircraft Exports</h3>
    <p>We source, inspect and deliver business and commercial aircraft to buyers around the globe, managing paperwork, ferry flights and registration from first contact to final handover.</p>
  </div>
  <div class="intro-col">
    <h3>Setup Of Air Services Worldwide</h3>
    <p>We plan and launch air services worldwide, from route studies and licensing to fleet selection, crew hiring and ground handling for new operators.</p>
  </div>
</section>

<section class="services">
  <svg class="title-mark" style="top:80px" viewBox="0 0 24 18"><path d="M2 12 L12 2 L22 12 L12 8 Z" fill="var(--gold)"/></svg>
  <h2 class="section-title" style="top:105px"><span class="gold">Our Product</span> <span class="red">And Services</span></h2>
  <svg width="1200" height="640" viewBox="0 0 1200 640">
    <g stroke="#5a5a5a" stroke-width="2" fill="none">
      <line x1="600" y1="300" x2="600" y2="265"/>
      <line x1="521" y1="355" x2="485" y2="340"/>
      <line x1="679" y1="355" x2="715" y2="340"/>
      <line x1="500" y1="445" x2="388" y2="500"/>
      <line x1="700" y1="445" x2="817" y2="500"/>
    </g>
    <circle cx="600" cy="410" r="118" fill="#1a1a1a" stroke="var(--gold)" stroke-width="8"/>
    <circle cx="600" cy="410" r="100" fill="#222"/>
    <text x="600" y="418" text-anchor="middle" font-family="Open Sans, Arial, sans-serif" font-weight="700" font-size="24" fill="var(--gold)">Veltrisk inc.</text>

    <g font-family="Open Sans, Arial, sans-serif" font-size="14" fill="#fff" font-weight="600">
      <circle cx="600" cy="265" r="36" fill="#2c2c2c" stroke="#777" stroke-width="2"/>
      <path d="M584 266 L616 262 L618 266 L616 270 Z M598 255 L606 264 L598 276 Z" fill="#fff"/>
      <text x="600" y="212" text-anchor="middle">Business Aircrafts</text>

      <circle cx="485" cy="340" r="36" fill="#2c2c2c" stroke="#777" stroke-width="2"/>
      <path d="M468 346 L502 334 L504 338 L472 350 Z M482 330 L492 342 L486 354 Z" fill="#fff"/>
      <text x="400" y="336" text-anchor="middle">Commercial</text>
      <text x="400" y="354" text-anchor="middle">Aircrafts</text>

      <circle cx="715" cy="340" r="36" fill="#2c2c2c" stroke="#777" stroke-width="2"/>
      <circle cx="715" cy="340" r="11" fill="none" stroke="#fff" stroke-width="4"/>
      <circle cx="715" cy="340" r="4" fill="#fff"/>
      <text x="800" y="336" text-anchor="middle">Operation</text>
      <text x="800" y="354" text-anchor="middle">Setup</text>

      <circle cx="350" cy="500" r="40" fill="var(--red)" stroke="#e04048" stroke-width="2"/>
      <path d="M332 502 L368 498 L370 502 L368 506 Z M348 490 L356 500 L348 512 Z" fill="#fff"/>
      <text x="255" y="494" text-anchor="middle">Amphibious</text>
      <text x="255" y="512" text-anchor="middle">Aircrafts</text>

      <circle cx="855" cy="500" r="36" fill="#2c2c2c" stroke="#777" stroke-width="2"/>
      <circle cx="855" cy="500" r="13" fill="none" stroke="#fff" stroke-width="5" stroke-dasharray="6 4"/>
      <circle cx="855" cy="500" r="5" fill="#fff"/>
      <text x="975" y="494" text-anchor="middle">Maintenance &amp;</text>
      <text x="975" y="512" text-anchor="middle">Crew Training</text>
    </g>
  </svg>
</section>

<section class="testimonials">
  <svg class="title-mark" style="top:60px" viewBox="0 0 24 18"><path d="M2 12 L12 2 L22 12 L12 8 Z" fill="var(--white)"/></svg>
  <h2 class="section-title" style="top:84px"><span class="gold">Client</span> Testimonials</h2>
  <div class="slide-arrow" style="left:128px">&lsaquo;</div>
  <div class="slide-arrow" style="left:1040px">&rsaquo;</div>
  <div class="quote quote-dark">Their team handled our export from start to finish. Every document was ready on time and the aircraft arrived in perfect condition.</div>
  <div class="quote quote-gold">A professional partner for our new air taxi service. The setup, training and support exceeded every expectation we had.</div>
  <div class="client" style="left:262px;top:340px">
    <div class="avatar" role="img" aria-label="Portrait photo of client Robert Danforth"></div>
    <div><div class="client-name">Robert Danforth</div><div class="stars">★★★★★</div></div>
  </div>
  <div class="client" style="left:650px;top:325px">
    <div class="avatar" role="img" aria-label="Portrait photo of client Elisa Marlowe"></div>
    <div><div class="client-name">Elisa Marlowe</div><div class="stars">★★★★★</div></div>
  </div>
</section>

<footer class="site-footer">
  <div class="foot-col" style="left:160px">
    <h4>Quick <span>Links</span></h4>
    <ul>
      <li>Home</li>
      <li>About Us</li>
      <li>Product And Services</li>
      <li>Contact Us</li>
    </ul>
    <div class="social"><span></span><span></span><span></span><span></span><span></span></div>
  </div>
  <div class="foot-col" style="left:410px">
    <h4>Contact <span>Details</span></h4>
    <div class="contact-line"><i></i>Veltrisk inc.</div>
    <div class="contact-line"><i></i>Marlow Fenwick Harbour Airfield</div>
    <div class="contact-line"><i></i>Hangar 6, Harbour Road</div>
    <div class="contact-line"><i></i>+1 (555) 014-7820</div>
    <div class="contact-line"><i></i>www.veltriskinc-example.com</div>
  </div>
  <div class="foot-col inquiry">
    <h4>Quick <span>Inquiry</span></h4>
    <div class="field">Name</div>
    <div class="field-row"><div class="field" style="width:80px">Email</div><div class="field" style="width:80px">Phone</div></div>
    <div class="field wide">Message</div>
    <div class="submit">SUBMIT</div>
  </div>
</footer>

<div class="copyright">Copyright © 2016 Veltrisk inc. All Rights Reserved</div>

</body>
</html>
```